Yard sign

I want it to look similar to this one,

change name to DRAVEK and submit new ideas

Also would like to improvise a bit. let's not make exactly the same thing

would like to change to: Connecticut #1 Company

also change phone to 203-555-0147
and website to
dravekllc.com

this is yard sign. size is 24' Width and 32' Height

Target Market(s)

Roof

Industry/Entity Type

Roofing

Requirements
Must have
• similar colors or add something new

```html
<!DOCTYPE html>
<html lang="en">
<head>
<meta charset="utf-8">
<title>DRAVEK Yard Sign</title>
<link rel="stylesheet" href="https://fonts.googleapis.com/css2?family=Rubik:wght@300;500;900&family=Titan+One&family=Barlow+Condensed:wght@800&display=swap">
<style>
  :root {
    --sign-black: #080808;
    --sign-brown: #3a2412;
    --sign-yellow: #f7e317;
    --gold-dark: #b5742a;
    --gold-mid: #e0a449;
    --gold-light: #ffe6b0;
    --accent-red: #e62128;
    --text-white: #ffffff;
    --text-black: #111111;
  }
  * { margin: 0; padding: 0; box-sizing: border-box; }
  html, body {
    width: 880px;
    height: 1200px;
    overflow: hidden;
    background: var(--sign-black);
  }
  .yard-sign {
    position: relative;
    width: 880px;
    height: 1200px;
    overflow: hidden;
    background: radial-gradient(ellipse at 62% 52%, var(--sign-brown) 0%, var(--sign-black) 55%);
  }
  .sign-backdrop {
    position: absolute;
    inset: 0;
    width: 100%;
    height: 100%;
  }
  .headline {
    position: absolute;
    left: 0;
    width: 100%;
    text-align: center;
    color: var(--text-white);
  }
  .headline-region {
    top: 100px;
    font-family: "Rubik", sans-serif;
    font-weight: 300;
    font-size: 78px;
    letter-spacing: 3px;
  }
  .headline-rank {
    top: 188px;
    font-family: "Rubik", sans-serif;
    font-weight: 900;
    font-size: 96px;
    letter-spacing: -1px;
  }
  .brand-name {
    position: absolute;
    top: 318px;
    left: 0;
    width: 100%;
    display: flex;
    justify-content: center;
    align-items: center;
    gap: 26px;
  }
  .brand-name-text {
    font-family: "Titan One", sans-serif;
    font-size: 158px;
    line-height: 1;
    color: var(--sign-yellow);
    letter-spacing: 4px;
  }
  .brand-mark-square {
    width: 54px;
    height: 54px;
    background: var(--accent-red);
  }
  .contact {
    position: absolute;
    left: 0;
    width: 100%;
    text-align: center;
    color: var(--text-black);
    line-height: 1;
  }
  .contact-phone {
    top: 900px;
    font-family: "Barlow Condensed", sans-serif;
    font-weight: 800;
    font-size: 132px;
    letter-spacing: 1px;
  }
  .contact-web {
    top: 1030px;
    font-family: "Rubik", sans-serif;
    font-weight: 500;
    font-size: 92px;
  }
</style>
</head>
<body>
  <main class="yard-sign">
    <svg class="sign-backdrop" viewBox="0 0 880 1200" aria-hidden="true">
      <defs>
        <linearGradient id="gold-sweep" x1="0" y1="0" x2="1" y2="0">
          <stop offset="0" stop-color="var(--gold-dark)"/>
          <stop offset="0.45" stop-color="var(--gold-mid)"/>
          <stop offset="0.62" stop-color="var(--gold-light)"/>
          <stop offset="1" stop-color="var(--gold-mid)"/>
        </linearGradient>
      </defs>
      <path class="gold-band" fill="url(#gold-sweep)"
            d="M0 370 C120 560 330 700 600 740 C720 756 820 740 880 720 L880 790 C740 860 560 880 430 850 C250 810 100 740 0 680 Z"/>
      <path class="gold-line" fill="none" stroke="var(--gold-light)" stroke-width="2" opacity="0.7"
            d="M0 470 C160 620 380 720 620 745 C740 752 830 740 880 728"/>
      <path class="yellow-field" fill="var(--sign-yellow)"
            d="M0 680 C140 770 300 850 470 845 C650 840 790 800 880 760 L880 1200 L0 1200 Z"/>
    </svg>

    <p class="headline headline-region">Connecticut</p>
    <p class="headline headline-rank">#1 Company</p>

    <div class="brand-name">
      <span class="brand-name-text">DRAVEK</span>
      <span class="brand-mark-square"></span>
    </div>

    <p class="contact contact-phone">203-555-0147</p>
    <p class="contact contact-web">dravekllc.com</p>
  </main>
</body>
</html>
```